Northgate Systems Line Card

I need to create a one page line card that displays the services that my company provides and the certifications we hold.
I have an updated logo that I will post as soon as I get it later today. For now you can see an example at:
The new logo is very close to this and the colors are the same.
The file that I have posted is an example of what I think is a slick format. the upload is a two page document, but I really only like the first page. What I need a little bit of marketing and then room for the content that describes our core services and certifications.
The content of the line card needs to be divided into 9 categories:
Cloud (Virtual) Computing environments
Links are to our current brochures on these items for reference.
Greetings all,
Greetings everyone!
Small to Medium sized businesses as well as government institutions. This should be a one page "firm handshake" type exposure that tells the customer they are dealing with a first class professional operation.
It Company

```html
<!DOCTYPE html>
<html lang="en">
<head>
<meta charset="utf-8">
<title>Northgate Systems – Line Card</title>
<link href="https://fonts.googleapis.com/css2?family=Mulish:wght@400;800&display=swap" rel="stylesheet">
<style>
  :root {
    --orange: #f47621;
    --ink: #231f20;
    --body: #4a4a4a;
    --stage: #e8e8e8;
    --paper: #ffffff;
    --card-top: #e3e3e4;
    --card-bottom: #ffffff;
    --white: #ffffff;
  }
  * { box-sizing: border-box; margin: 0; padding: 0; }
  html, body { width: 1040px; height: 1200px; overflow: hidden; }
  body {
    background: var(--stage);
    font-family: "Mulish", "Century Gothic", sans-serif;
    position: relative;
  }
  .line-card {
    position: absolute;
    left: 100px; top: 56px;
    width: 840px; height: 1088px;
    background: linear-gradient(180deg, #fafafa 0%, var(--paper) 40%, #f6f6f6 100%);
    box-shadow: 0 6px 24px rgba(0,0,0,.18);
    overflow: hidden;
  }
  .header-band, .footer-band { position: absolute; left: 0; }
  .header-band { top: 0; width: 840px; height: 215px; }
  .footer-band { top: 1008px; width: 840px; height: 80px; }

  .brand {
    position: absolute; top: 78px; left: 0; width: 840px;
    text-align: center; color: var(--ink);
  }
  .brand-name {
    display: inline-flex; align-items: center; gap: 14px;
    font-weight: 800; font-size: 38px; letter-spacing: 1px; line-height: 1;
  }
  .brand-mark { width: 34px; height: 34px; background: var(--ink); }
  .brand-tagline {
    margin-top: 12px; font-weight: 800; font-size: 12px; letter-spacing: 1px;
  }

  .services {
    position: absolute; left: 33px; top: 253px;
    display: grid;
    grid-template-columns: repeat(3, 248px);
    grid-template-rows: 217px 217px 217px;
    column-gap: 18px;
    row-gap: 32px;
  }
  .services .service-card:nth-child(n+7) { margin-top: -8px; }
  .service-card {
    background: linear-gradient(180deg, var(--card-top) 0%, var(--card-bottom) 55%, #f4f4f4 100%);
    box-shadow: 2px 4px 8px rgba(0,0,0,.28);
    padding: 10px 12px 0 12px;
  }
  .service-title {
    font-weight: 800; font-size: 24px; color: var(--ink); line-height: 1.1;
  }
  .service-lead {
    margin-top: 6px; font-size: 13.5px; line-height: 15px; color: var(--orange);
  }
  .service-text {
    margin-top: 10px; font-size: 10px; line-height: 11.6px; color: var(--body);
    text-align: justify;
  }

  .contact {
    position: absolute; top: 1010px; left: 0; width: 840px;
    text-align: center; color: var(--white);
    font-size: 13px; line-height: 15px;
  }
  .contact-lines { margin-top: 10px; }
  .contact .sep { margin: 0 6px; }
</style>
</head>
<body>
  <main class="line-card">
    <svg class="header-band" viewBox="0 0 840 215" aria-hidden="true">
      <polygon points="29,0 814,0 814,74 673,215 173,215 29,74" fill="var(--orange)"/>
      <rect x="216" y="0" width="111" height="22" fill="var(--paper)"/>
      <rect x="515" y="0" width="111" height="22" fill="var(--paper)"/>
    </svg>

    <header class="brand">
      <div class="brand-name"><span class="brand-mark"></span>NORTHGATE SYSTEMS</div>
      <p class="brand-tagline">ENTERPRISE SOLUTIONS FOR EVERYONE</p>
    </header>

    <section class="services">
      <article class="service-card">
        <h2 class="service-title">Outsourced IT</h2>
        <p class="service-lead">Northgate Systems provides customized Proactive IT monitoring and support</p>
        <p class="service-text">Lorem ipsum dolor sit amet, consectetur adipiscing elit. Ut porta ac tortor vitae mollis. Vestibulum nec aliquam enim. Phasellus at leo nec libero ornare hendrerit viverra nec erat. Donec ultrices pharetra nulla vel porttitor. Sed laoreet tortor fringilla, hendrerit quam vulputate, aliquet mauris. Pellentesque habitant morbi tristique senectus et netus et malesuada fames ac turpis egestas.</p>
      </article>
      <article class="service-card">
        <h2 class="service-title">Outsourced IT</h2>
        <p class="service-lead">Northgate Systems provides customized Proactive IT monitoring and support</p>
        <p class="service-text">Lorem ipsum dolor sit amet, consectetur adipiscing elit. Ut porta ac tortor vitae mollis. Vestibulum nec aliquam enim. Phasellus at leo nec libero ornare hendrerit viverra nec erat. Donec ultrices pharetra nulla vel porttitor. Sed laoreet tortor fringilla, hendrerit quam vulputate, aliquet mauris. Pellentesque habitant morbi tristique senectus et netus et malesuada fames ac turpis egestas.</p>
      </article>
      <article class="service-card">
        <h2 class="service-title">Outsourced IT</h2>
        <p class="service-lead">Northgate Systems provides customized Proactive IT monitoring and support</p>
        <p class="service-text">Lorem ipsum dolor sit amet, consectetur adipiscing elit. Ut porta ac tortor vitae mollis. Vestibulum nec aliquam enim. Phasellus at leo nec libero ornare hendrerit viverra nec erat. Donec ultrices pharetra nulla vel porttitor. Sed laoreet tortor fringilla, hendrerit quam vulputate, aliquet mauris. Pellentesque habitant morbi tristique senectus et netus et malesuada fames ac turpis egestas.</p>
      </article>
      <article class="service-card">
        <h2 class="service-title">Outsourced IT</h2>
        <p class="service-lead">Northgate Systems provides customized Proactive IT monitoring and support</p>
        <p class="service-text">Lorem ipsum dolor sit amet, consectetur adipiscing elit. Ut porta ac tortor vitae mollis. Vestibulum nec aliquam enim. Phasellus at leo nec libero ornare hendrerit viverra nec erat. Donec ultrices pharetra nulla vel porttitor. Sed laoreet tortor fringilla, hendrerit quam vulputate, aliquet mauris. Pellentesque habitant morbi tristique senectus et netus et malesuada fames ac turpis egestas.</p>
      </article>
      <article class="service-card">
        <h2 class="service-title">Outsourced IT</h2>
        <p class="service-lead">Northgate Systems provides customized Proactive IT monitoring and support</p>
        <p class="service-text">Lorem ipsum dolor sit amet, consectetur adipiscing elit. Ut porta ac tortor vitae mollis. Vestibulum nec aliquam enim. Phasellus at leo nec libero ornare hendrerit viverra nec erat. Donec ultrices pharetra nulla vel porttitor. Sed laoreet tortor fringilla, hendrerit quam vulputate, aliquet mauris. Pellentesque habitant morbi tristique senectus et netus et malesuada fames ac turpis egestas.</p>
      </article>
      <article class="service-card">
        <h2 class="service-title">Outsourced IT</h2>
        <p class="service-lead">Northgate Systems provides customized Proactive IT monitoring and support</p>
        <p class="service-text">Lorem ipsum dolor sit amet, consectetur adipiscing elit. Ut porta ac tortor vitae mollis. Vestibulum nec aliquam enim. Phasellus at leo nec libero ornare hendrerit viverra nec erat. Donec ultrices pharetra nulla vel porttitor. Sed laoreet tortor fringilla, hendrerit quam vulputate, aliquet mauris. Pellentesque habitant morbi tristique senectus et netus et malesuada fames ac turpis egestas.</p>
      </article>
      <article class="service-card">
        <h2 class="service-title">Outsourced IT</h2>
        <p class="service-lead">Northgate Systems provides customized Proactive IT monitoring and support</p>
        <p class="service-text">Lorem ipsum dolor sit amet, consectetur adipiscing elit. Ut porta ac tortor vitae mollis. Vestibulum nec aliquam enim. Phasellus at leo nec libero ornare hendrerit viverra nec erat. Donec ultrices pharetra nulla vel porttitor. Sed laoreet tortor fringilla, hendrerit quam vulputate, aliquet mauris. Pellentesque habitant morbi tristique senectus et netus et malesuada fames ac turpis egestas.</p>
      </article>
      <article class="service-card">
        <h2 class="service-title">Outsourced IT</h2>
        <p class="service-lead">Northgate Systems provides customized Proactive IT monitoring and support</p>
        <p class="service-text">Lorem ipsum dolor sit amet, consectetur adipiscing elit. Ut porta ac tortor vitae mollis. Vestibulum nec aliquam enim. Phasellus at leo nec libero ornare hendrerit viverra nec erat. Donec ultrices pharetra nulla vel porttitor. Sed laoreet tortor fringilla, hendrerit quam vulputate, aliquet mauris. Pellentesque habitant morbi tristique senectus et netus et malesuada fames ac turpis egestas.</p>
      </article>
      <article class="service-card">
        <h2 class="service-title">Outsourced IT</h2>
        <p class="service-lead">Northgate Systems provides customized Proactive IT monitoring and support</p>
        <p class="service-text">Lorem ipsum dolor sit amet, consectetur adipiscing elit. Ut porta ac tortor vitae mollis. Vestibulum nec aliquam enim. Phasellus at leo nec libero ornare hendrerit viverra nec erat. Donec ultrices pharetra nulla vel porttitor. Sed laoreet tortor fringilla, hendrerit quam vulputate, aliquet mauris. Pellentesque habitant morbi tristique senectus et netus et malesuada fames ac turpis egestas.</p>
      </article>
    </section>

    <svg class="footer-band" viewBox="0 0 840 80" aria-hidden="true">
      <polygon points="164,0 664,0 744,80 86,80" fill="var(--orange)"/>
    </svg>

    <footer class="contact">
      <p>1200 Alder Crest Way</p>
      <p>Riverton, Oregon 97400</p>
      <p class="contact-lines">555-014-2290<span class="sep">|</span>www.northgatesys.com<span class="sep">|</span>support@northgatesys.com</p>
    </footer>
  </main>
</body>
</html>
```